Marla Tovesby, Broker Associate

I need a new business card for my Real Estate services. I am a Broker Associate and also have my MBA. I am a PA too. I would like to have it say "Third Generation Selling" too some where. I like the bold look of cards and I think I am leaning towards a black or dark background. I need it to tie in my logo with the Pinegate Marsden Vic Olander Realty logo. I like the foil and shiny look of some letters too. I might add my picture but would like to see some with out my picture too. I sell a lot of lakefront homes but I don't want it to be focused on water. Maybe subtle?

Target Market(s)

18+

Industry/Entity Type

Real Estate Agent

Contact Information for Business Card

The design must have my logo and Pinegate Marsden logo.
My name: Marla Tovesby
My cell phone 555-318-2976
business address: 4820 West Orchard Road Larkmere, ST 00000
Office phone: 555-762-0158
email: MarlaJTovesby@mailbrook.test
website: www.BrightporchHomes.test
Facebook: www.facebook.com/marlabrightporchhomes
Also 'Third Generation Selling' and Realtor logo must be on it.

Font styles to use
Sans Serif

Colors
0555a3
000000
ffffff
d3d3d3
3176b5

Requirements
Must have
• I want this to stand out from all the other Realtors. I like bold look. I need it to match my logo and tie in the Pinegate Marsden logo. I can do front and back on card. The office details can be smaller than my name and information.
Nice to have
• I like the foil look and matte as well. I want something bold that stands out.

```html
<!DOCTYPE html>
<html lang="en">
<head>
<meta charset="utf-8">
<title>Marla Tovesby – Business Card</title>
<link href="https://fonts.googleapis.com/css2?family=Roboto+Condensed:wght@400;500&family=Roboto:wght@400;500&display=swap" rel="stylesheet">
<style>
  :root {
    --backdrop: #3a332f;
    --card: #1c2024;
    --card-edge: #111417;
    --silver: #c9cbcd;
    --silver-dim: #8d9094;
    --blue: #1f7fd1;
    --blue-deep: #0555a3;
    --white: #ffffff;
    --grey: #d3d3d3;
  }
  * { margin: 0; padding: 0; box-sizing: border-box; }
  html, body { width: 1200px; height: 769px; overflow: hidden; }
  body {
    background: var(--backdrop);
    font-family: "Roboto", Arial, sans-serif;
    position: relative;
  }
  .card {
    position: absolute;
    top: 230px;
    width: 540px;
    height: 309px;
    background: var(--card);
    border: 1px solid var(--card-edge);
    box-shadow: 0 10px 24px rgba(0,0,0,.45);
  }
  .card--front { left: 45px; }
  .card--back { left: 615px; }

  /* Front */
  .brand {
    position: absolute;
    left: 70px; top: 110px;
    display: flex; align-items: center; gap: 14px;
  }
  .brand__mark { width: 22px; height: 22px; background: var(--silver); }
  .brand__name {
    font-family: "Roboto Condensed", Arial, sans-serif;
    font-weight: 500; font-size: 38px; letter-spacing: 2px;
    text-transform: uppercase; color: var(--silver);
  }
  .tagline {
    position: absolute; left: 70px; top: 190px;
    font-size: 15px; color: var(--silver-dim); letter-spacing: .5px;
  }
  .affiliations {
    position: absolute; right: 28px; top: 26px;
    display: flex; align-items: flex-start; gap: 16px;
  }
  .badge { width: 30px; height: 30px; background: var(--silver-dim); }
  .brokerage { display: flex; align-items: center; gap: 6px; }
  .brokerage__mark { width: 14px; height: 14px; background: var(--blue-deep); }
  .brokerage__name {
    font-family: "Roboto Condensed", Arial, sans-serif;
    font-size: 10px; line-height: 1.25; color: var(--grey);
    text-transform: uppercase;
  }

  /* Back */
  .agent-name {
    position: absolute; left: 28px; top: 26px;
    font-family: "Roboto Condensed", Arial, sans-serif;
    font-weight: 500; font-size: 21px; color: var(--blue);
    text-transform: uppercase;
  }
  .contact-list {
    position: absolute; left: 28px; top: 130px;
    list-style: none;
  }
  .contact-list li {
    display: flex; align-items: center; gap: 10px;
    font-size: 14px; line-height: 19px; color: var(--white);
  }
  .contact-list svg { width: 12px; height: 12px; fill: var(--blue); flex: none; }
  .divider {
    position: absolute; left: 28px; width: 330px; top: 240px;
    height: 1px; background: var(--white);
  }
  .office-address {
    position: absolute; left: 28px; top: 252px;
    font-size: 14px; color: var(--white);
  }
  .back-brand {
    position: absolute; right: 26px; bottom: 32px;
    display: flex; align-items: center; gap: 8px;
  }
  .back-brand__mark { width: 16px; height: 16px; background: var(--blue); }
  .back-brand__name {
    font-family: "Roboto Condensed", Arial, sans-serif;
    font-weight: 500; font-size: 20px; color: var(--white);
    text-transform: uppercase; line-height: 1;
  }
</style>
</head>
<body>
  <section class="card card--front">
    <div class="affiliations">
      <div class="badge" role="img" aria-label="Partner membership badge"></div>
      <div class="brokerage">
        <span class="brokerage__mark"></span>
        <span class="brokerage__name">Pinegate Marsden<br>Vic Olander Realty</span>
      </div>
    </div>
    <div class="brand">
      <span class="brand__mark"></span>
      <span class="brand__name">Marla Tovesby</span>
    </div>
    <p class="tagline">Third Generation Selling</p>
  </section>

  <section class="card card--back">
    <h1 class="agent-name">Marla Tovesby</h1>
    <ul class="contact-list">
      <li><svg viewBox="0 0 12 12"><path d="M2 1h3l1 3-2 1a7 7 0 0 0 3 3l1-2 3 1v3c-6 0-9-3-9-9z"/></svg>555-762-0158</li>
      <li><svg viewBox="0 0 12 12"><path d="M3 0h6v12H3zM4 1v9h4V1z"/></svg>555-318-2976</li>
      <li><svg viewBox="0 0 12 12"><path d="M0 2h12v8H0zM1 3l5 4 5-4z"/></svg>MarlaJTovesby@mailbrook.test</li>
      <li><svg viewBox="0 0 12 12"><circle cx="6" cy="6" r="6"/></svg>www.BrightporchHomes.test</li>
      <li><svg viewBox="0 0 12 12"><rect width="12" height="12"/></svg>/marlabrightporchhomes</li>
    </ul>
    <div class="divider"></div>
    <p class="office-address">4820 West Orchard Road Larkmere, ST 00000</p>
    <div class="back-brand">
      <span class="back-brand__mark"></span>
      <span class="back-brand__name">Marla Tovesby</span>
    </div>
  </section>
</body>
</html>
```